Flyer-Design für Abschleppunternehmen
Zielgruppe
Wir sind ein Abschleppunternehmen und sind bestrebt neue Kunden zu gewinnen. Vor allem im Bereich 'Falschparker' suchen wir Firmen/Unternehmen mit Privatparkplätzen, die von fremden Personen zu geparkt werden. Hierzu ist stark darauf hinzuweisen, dass diese Leistung für den Autraggeber völlig kostenlos und ohne Aufwand anzufordern ist.
Aufgabenstellung
Vorschlag DIN Fyler 21x9,8cm . Wir sind ein 24/7 Betrieb. Rufnr. 083547918. Es ist darauf hinzweisen, dass wir ein unternehmen aus der direkten umgebung sind.

```html
<!DOCTYPE html>
<html lang="de">
<head>
<meta charset="utf-8">
<title>Brenninger Abschleppdienst – Flyer</title>
<link rel="stylesheet" href="https://fonts.googleapis.com/css2?family=Roboto:ital,wght@0,400;0,500;0,700;0,900;1,500;1,700&display=swap">
<style>
  :root {
    --bg: #dcdcdc;
    --paper: #f4f4f4;
    --white: #ffffff;
    --red: #d7141a;
    --yellow: #f5cf00;
    --yellow-band: #e8c300;
    --ink: #111111;
    --grey-text: #555555;
    --sign-blue: #2a8fd8;
    --photo-garage: linear-gradient(160deg, #9a9a9a 0%, #c9c9c9 35%, #d9b820 60%, #8a8a8a 100%);
    --photo-street: linear-gradient(175deg, #8d8d8d 0%, #b9b9b9 45%, #d7b51c 70%, #6e6e6e 100%);
    --photo-autumn: linear-gradient(180deg, #6f6e6a 0%, #b07a3a 40%, #e0b81a 65%, #5a5a5a 100%);
  }
  * { box-sizing: border-box; margin: 0; padding: 0; }
  html, body {
    width: 1200px; height: 900px; overflow: hidden;
    background: var(--bg);
    font-family: "Roboto", Arial, sans-serif;
    color: var(--ink);
  }
  .stage { position: relative; width: 1200px; height: 900px; }

  .flyer {
    position: absolute; top: 50px;
    width: 374px; height: 800px;
    background: var(--paper);
    box-shadow: 0 10px 30px rgba(0,0,0,.18);
    overflow: hidden;
  }
  .flyer--front { left: 196px; }
  .flyer--back { left: 630px; background: var(--white); }

  /* Front */
  .brand {
    position: absolute; left: 26px; top: 30px;
    display: flex; align-items: center; gap: 8px;
    font-size: 22px; font-weight: 700; color: var(--red);
  }
  .brand__mark { width: 14px; height: 14px; background: var(--red); }

  .no-parking { position: absolute; right: 26px; top: 74px; width: 54px; height: 54px; }

  .headline {
    position: absolute; left: 22px; right: 18px; top: 140px;
    font-size: 31px; font-weight: 900; color: var(--red); letter-spacing: -.3px;
    white-space: nowrap;
  }

  .subline {
    position: absolute; left: 0; right: 0; top: 190px;
    display: flex; align-items: center; gap: 12px;
    font-size: 17px; font-weight: 400;
  }
  .subline::before, .subline::after { content: ""; flex: 1; height: 1.5px; background: var(--ink); }

  .hero-photo {
    position: absolute; left: 0; right: 0; top: 226px; height: 280px;
    background: var(--photo-garage);
  }
  .badge-years {
    position: absolute; left: 28px; top: 440px;
    width: 128px; height: 128px; border-radius: 50%;
    background: #1b1b1b; color: var(--white);
    display: flex; flex-direction: column; align-items: center; justify-content: center;
    font-size: 25px; line-height: 1.05;
  }
  .badge-years strong { font-weight: 900; font-size: 32px; }

  .region {
    position: absolute; left: 24px; top: 588px; right: 20px;
    font-size: 22px; font-weight: 900; line-height: 1.35;
  }
  .mark {
    background: linear-gradient(transparent 45%, var(--yellow) 45%, var(--yellow) 92%, transparent 92%);
    padding: 0 4px;
  }
  .pitch {
    position: absolute; left: 24px; top: 656px; right: 20px;
    font-size: 15.5px; line-height: 1.3;
  }
  .pitch strong { font-weight: 900; }
  .pitch__cta { display: block; margin-top: 8px; font-weight: 700; }

  .hotline {
    position: absolute; left: 0; right: 0; bottom: 0; height: 60px;
    background: var(--yellow-band);
    display: flex; align-items: center; gap: 26px; padding-left: 24px;
    font-size: 17px; font-style: italic;
  }
  .hotline__number { font-weight: 700; }
  .hotline__label { font-weight: 500; }

  /* Back */
  .services-title {
    position: absolute; left: 24px; top: 44px;
    font-size: 19px; font-weight: 700; color: #333;
  }
  .services {
    position: absolute; left: 26px; top: 100px;
    list-style: none; font-size: 15.5px; color: var(--grey-text);
  }
  .services li { display: flex; gap: 12px; line-height: 34.5px; }
  .services li::before { content: "*"; font-weight: 700; font-size: 20px; color: #444; width: 10px; }
  .service-247 { position: absolute; right: 28px; top: 218px; width: 78px; height: 78px; }

  .gallery {
    position: absolute; left: 0; right: 0; top: 360px; height: 368px;
    display: grid; grid-template-columns: 136px 1fr; grid-template-rows: 190px 1fr; gap: 8px;
  }
  .gallery__photo--street { background: var(--photo-street); }
  .gallery__photo--garage { background: var(--photo-garage); }
  .gallery__photo--truck { grid-column: 1 / 3; background: var(--photo-autumn); }
  .flyer--back .hotline { height: 64px; }
</style>
</head>
<body>
<main class="stage">

  <section class="flyer flyer--front">
    <div class="brand"><span class="brand__mark"></span>Brenninger</div>

    <svg class="no-parking" viewBox="0 0 58 58" aria-hidden="true">
      <circle cx="29" cy="29" r="25" fill="var(--sign-blue)" stroke="var(--red)" stroke-width="7"/>
      <line x1="13" y1="13" x2="45" y2="45" stroke="var(--red)" stroke-width="6"/>
      <line x1="45" y1="13" x2="13" y2="45" stroke="var(--red)" stroke-width="6"/>
    </svg>
    <h1 class="headline">Falschparker gesehen?</h1>
    <p class="subline">Wir erledigen das für Sie!</p>

    <div class="hero-photo" role="img" aria-label="Gelber Abschlepp-Pickup in einer Tiefgarage neben einem geparkten Auto"></div>
    <div class="badge-years"><span>Seit <strong>50</strong></span><span>Jahren</span></div>

    <h2 class="region"><span class="mark">Wir sind Ihr Abschleppdienst</span><br><span class="mark">der Region.</span></h2>
    <p class="pitch">Lassen Sie unberechtigt geparkte Fahrzeuge <strong>kostenlos</strong> abschleppen!
      <span class="pitch__cta">Ein Anruf genügt.</span></p>

    <footer class="hotline">
      <span class="hotline__number">+49 8354 7918</span>
      <span class="hotline__label">24/7 Service-Hotline</span>
    </footer>
  </section>

  <section class="flyer flyer--back">
    <h2 class="services-title"><span class="mark">Wir können auch mehr!</span></h2>
    <ul class="services">
      <li>PKW Abschlepp- Bergungsdienst</li>
      <li>LKW Abschlepp- Bergungsdienst</li>
      <li>Kranservice</li>
      <li>Fahrzeugtransporte</li>
      <li>Ölspurbeseitigung</li>
      <li>Fahrzeugöffnungen</li>
    </ul>
    <svg class="service-247" viewBox="0 0 78 78" aria-label="24/7 Service">
      <path d="M62 14 A34 34 0 1 0 72 39" fill="none" stroke="#333" stroke-width="2"/>
      <path d="M54 10 L64 13 L60 23" fill="none" stroke="#333" stroke-width="2"/>
      <text x="39" y="40" text-anchor="middle" font-family="Roboto, sans-serif" font-size="19" font-weight="500" fill="#333">24/7</text>
      <text x="39" y="54" text-anchor="middle" font-family="Roboto, sans-serif" font-size="9" font-weight="700" fill="#333">SERVICE</text>
    </svg>

    <div class="gallery">
      <div class="gallery__photo--street" role="img" aria-label="Gelber Pickup vor einer Garageneinfahrt"></div>
      <div class="gallery__photo--garage" role="img" aria-label="Gelber Pickup in einem Parkhaus"></div>
      <div class="gallery__photo--truck" role="img" aria-label="Großer gelber Abschlepp-LKW vor herbstlichen Bäumen"></div>
    </div>

    <footer class="hotline">
      <span class="hotline__number">+49 8354 7918</span>
      <span class="hotline__label">24/7 Service-Hotline</span>
    </footer>
  </section>

</main>
</body>
</html>
```